Two sided business card template for:

Room 4 Keeps Storage
1817 Brantley Avenue,
Saskatoon, SK
R3P 2W6
306-555-0184
www.room4keeps.ca

Front side should be standard business card information. Sample should be for Gregory Lindell, Operations Manager, greg@room4keeps.ca

Back side should be an advertisement for the storage facility. Some points about our facility are below you may use some or all of these features in the ad.

-Online payments and bookings
-Seasonal bicycle, tire, and motorcycle storage
-24hr self storage access
-Safe, and secure, with digital video surveillance
-Airport location

Card could have, but doesn't need a clever tag line containing the company name

Finished design must be in Microsoft word, or publisher format, and text must be editable.

```html
<!DOCTYPE html>
<html lang="en">
<head>
<meta charset="utf-8">
<title>Room 4 Keeps Storage – Business Card</title>
<link href="https://fonts.googleapis.com/css2?family=Arimo:wght@400;700&display=swap" rel="stylesheet">
<style>
  :root {
    --brand-red: #d9171b;
    --card-white: #ffffff;
    --ink: #111111;
    --peach: #efa88a;
    --backdrop: #e9e6e2;
  }
  * { margin: 0; padding: 0; box-sizing: border-box; }
  html, body {
    width: 1200px; height: 960px; overflow: hidden;
    background: var(--backdrop);
    font-family: "Arimo", Arial, sans-serif;
  }
  .canvas {
    position: relative; width: 1200px; height: 960px;
    display: flex; justify-content: center; align-items: center; gap: 90px;
  }
  .card {
    position: relative; width: 400px; height: 700px; overflow: hidden;
    box-shadow: 0 6px 18px rgba(0,0,0,0.18);
  }

  /* Back side: advertisement */
  .card--back { background: var(--brand-red); color: var(--card-white); }
  .feature-list {
    list-style: none; position: absolute; top: 92px; left: 30px; right: 30px;
    text-align: center; font-size: 17px; line-height: 1.55;
  }
  .unit-illustration {
    position: absolute; left: 0; bottom: 0; width: 400px; height: 300px;
    background: linear-gradient(160deg, #e55a3e 0%, var(--peach) 100%);
  }

  /* Front side: contact card */
  .card--front { background: var(--card-white); }
  .front-band { position: absolute; left: 0; top: 0; width: 400px; height: 700px; }
  .brand {
    position: absolute; top: 118px; left: 0; right: 0;
    display: flex; justify-content: center; align-items: center; gap: 12px;
  }
  .brand__mark { width: 26px; height: 26px; background: var(--brand-red); }
  .brand__name {
    font-weight: 700; font-size: 27px; color: var(--ink); letter-spacing: 0.5px;
  }
  .person { position: absolute; top: 318px; left: 0; right: 0; text-align: center; }
  .person__name { font-weight: 700; font-size: 28px; color: var(--ink); }
  .person__title { font-size: 16px; color: var(--ink); margin-top: 4px; }
  .contact {
    list-style: none; position: absolute; top: 448px; left: 0; right: 0;
    text-align: center; color: var(--card-white); font-size: 19px; line-height: 1.6;
  }
</style>
</head>
<body>
<main class="canvas">
  <section class="card card--back" aria-label="Card back">
    <ul class="feature-list">
      <li>Online payments and bookings</li>
      <li>Seasonal bicycle, tire, and motorcycle storage</li>
      <li>24hr self storage access</li>
      <li>Safe, and secure, with digital video surveillance</li>
      <li>Airport location</li>
    </ul>
    <div class="unit-illustration" role="img" aria-label="Illustration of a storage unit with a roll-up door and a keyhole"></div>
  </section>

  <section class="card card--front" aria-label="Card front">
    <svg class="front-band" viewBox="0 0 400 700" aria-hidden="true">
      <path d="M0 250 Q200 200 400 300 L400 700 L0 700 Z" fill="var(--brand-red)"/>
    </svg>
    <div class="brand">
      <span class="brand__mark"></span>
      <span class="brand__name">Room 4 Keeps Storage</span>
    </div>
    <div class="person">
      <h1 class="person__name">Gregory Lindell</h1>
      <p class="person__title">Operations Manager</p>
    </div>
    <ul class="contact">
      <li>306-555-0184</li>
      <li>www.room4keeps.ca</li>
      <li>greg@room4keeps.ca</li>
      <li>1817 Brantley Avenue,</li>
      <li>Saskatoon, SK R3P 2W6</li>
    </ul>
  </section>
</main>
</body>
</html>
```